Design of a promotional offer flyer required to promote low-cost websites to 1-man band businesses

I want a flyer designed - either a double-sided A5 flyer or even A4 folded into a third double-sided. The flyer is to showcase a new service - low-cost websites for 1-man-band businesses, business startups and tradesmen in England. Look at the copy, find some pix and let me know! Flyer will be printed and used as an image on my website too. Pix could be related to some of the target groups. We need to stress the simple message that websites start from £5 per week and this is an-all-in-one fee.

Target Market(s)

Tradesmen, business start ups and 1-man band businesses that want a website

Industry/Entity Type

Small Business

Contact Information for Business Card

All contact details and name of business to be confirmed shortly

Font styles to use
Serif

Requirements
Must have
• Basic messages from copy for flyer i.e. websites from £5 per week and what each client gets for that price to be included on the business card! Please read copy for the flyer.
Nice to have
• Nice background image or series of small images relevant to the target audience. Again, see list of targets from copy for flyer.
Should not have
• I don't want exact or similar design to my main business Blue Harbour Promotions. The new flyer and business card should be a different and distinct branding to that of Blue Harbour Promotions. Aimed at a more economical style, whilst looking professional, but relevant to the target audiences.

```html
<!DOCTYPE html>
<html lang="en">
<head>
<meta charset="utf-8">
<title>Low-cost websites flyer</title>
<link href="https://fonts.googleapis.com/css2?family=Source+Sans+3:wght@400;600;700;800;900&display=swap" rel="stylesheet">
<style>
:root{
  --stage:#2b2b2b;
  --navy:#0a2140;
  --orange:#f7941d;
  --orange-hot:#ff5a00;
  --orange-band:#ef7d1a;
  --blue:#0b76c2;
  --yellow:#f5d33b;
  --red-dark:#c8102e;
  --red:#e31b2d;
  --ink:#1a1a1a;
  --white:#ffffff;
}
*{margin:0;padding:0;box-sizing:border-box}
html,body{width:1200px;height:857px;overflow:hidden;background:var(--stage)}
body{position:relative;font-family:"Source Sans 3",sans-serif}
.page{position:absolute;top:86px;width:483px;height:686px;overflow:hidden}

/* front */
.front{left:101px;background:linear-gradient(180deg,#0a1c36 0%,#0f3562 30%,#2f79b0 50%,#9cc6e4 60%,#ffffff 70%,#ffffff 100%)}
.front .headline{position:absolute;left:0;width:100%;top:38px;text-align:center;color:var(--orange);font-weight:800;font-size:53px;letter-spacing:0.5px;line-height:1}
.front .subhead{position:absolute;left:0;width:100%;top:88px;text-align:center;color:var(--white);font-weight:700;font-size:28px;line-height:1}
.front .showcase{position:absolute;left:34px;top:153px;width:425px;height:162px;background:linear-gradient(180deg,#d9e4ee 0%,#6f8fae 55%,rgba(40,90,140,0.3) 100%);border-radius:2px}
.front .audience-lead{position:absolute;left:0;width:100%;top:341px;text-align:center;color:var(--white);font-weight:700;font-size:15.5px;line-height:17px}
.price{position:absolute;left:45px;top:392px;white-space:nowrap}
.price .only{font-weight:800;font-size:122px;color:var(--blue);letter-spacing:-1px;line-height:1}
.price .amount{font-weight:800;font-size:122px;color:var(--orange-hot);margin-left:22px;line-height:1}
.price .per{position:absolute;left:263px;top:102px;font-weight:700;font-size:29px;color:var(--ink)}
.front .no-upfront{position:absolute;left:0;width:100%;top:532px;text-align:center;color:var(--blue);font-weight:700;font-size:40px;line-height:1}
.front .suitable{position:absolute;left:20px;width:443px;top:585px;text-align:center;color:var(--ink);font-size:12.6px;line-height:16.8px;white-space:nowrap}

/* back */
.back{left:608px;background:linear-gradient(180deg,#0b2748 0%,#1a4f86 45%,#1e5a94 62%,#16426f 68%)}
.back .topband{position:absolute;left:0;top:0;width:100%;height:41px;background:var(--navy)}
.back .section-title{position:absolute;left:30px;top:16px;color:var(--white);font-weight:700;font-size:18px}
.benefits{position:absolute;left:30px;top:47px;width:446px;list-style:none;color:var(--white);font-size:14px;line-height:18px}
.benefits li{position:relative;padding-left:17px;white-space:nowrap}
.benefits svg{position:absolute;left:0;top:4px;width:12px;height:11px}
.back .fee{position:absolute;left:0;width:100%;top:312px;text-align:center;color:var(--yellow);font-weight:700;font-size:15.5px;line-height:18px}
.back .trades-photos{position:absolute;left:0;top:354px;width:100%;height:100px;display:flex}
.trades-photos div{flex:1}
.photo-electrician{background:linear-gradient(135deg,#e9e6e1,#8c7a68)}
.photo-tiler{background:linear-gradient(135deg,#efe9e4,#b55a4a)}
.photo-plumber{background:linear-gradient(135deg,#d6d3cf,#7d6a5a)}
.offer-band{position:absolute;left:0;top:452px;width:100%;height:48px;background:var(--red-dark)}
.offer-band .promo{position:absolute;left:31px;top:4px;color:var(--white);font-weight:800;font-size:40px;line-height:40px;letter-spacing:0.5px}
.offer-tab{position:absolute;left:290px;top:444px;width:193px;height:48px}
.offer-tab span{position:absolute;left:40px;top:2px;color:var(--white);font-weight:800;font-size:39px;line-height:40px}
.orange-band{position:absolute;left:0;top:500px;width:100%;height:86px;background:var(--orange-band);text-align:center;color:var(--white);font-weight:700;font-size:20px;line-height:22px;padding-top:9px}
.contact{position:absolute;left:0;top:586px;width:100%;height:100px;background:var(--white);text-align:center;color:var(--ink)}
.contact .line{font-size:11.5px;line-height:15px;display:flex;justify-content:center;align-items:center;gap:4px}
.contact .line svg{width:10px;height:10px}
.contact .address{margin-top:8px}
.contact .gap{margin-left:8px}
.call{font-size:27px;line-height:30px;margin-top:6px}
.call .number{font-weight:700;border-left:2px solid var(--ink);padding-left:6px;margin-left:4px}
.contact .terms{font-size:11.3px;margin-top:4px}
</style>
</head>
<body>

<section class="page front">
  <h1 class="headline">WANT A WEBSITE ?</h1>
  <p class="subhead">WITHOUT IT COSTING THE EARTH?</p>
  <div class="showcase" role="img" aria-label="Fanned display of example website layouts on screens"></div>
  <p class="audience-lead">PROFESSIONALLY-DESIGNED WEBSITES FOR TRADESMEN,<br>BUSINESS START-UPS AND 1-MAN BANDS FROM</p>
  <div class="price">
    <span class="only">only</span><span class="amount">£5</span>
    <span class="per">per week</span>
  </div>
  <p class="no-upfront">and NO upfront costs!</p>
  <p class="suitable">Suitable for plumbers, electricians, roofers, builders, painters and decorators,<br>joiners, business start-ups, 1-man bands such as hairdressers, photographers, fit-<br>ness instructors, window cleaners, beauticians, gardeners, odd job men, wheelie<br>bin cleaners, IFAs or self-employed consultants.</p>
</section>

<section class="page back">
  <div class="topband"></div>
  <h2 class="section-title">Here’s what you get</h2>
  <ul class="benefits">
    <li><svg viewBox="0 0 12 11"><path d="M1 6l3 3 7-8" fill="none" stroke="#fff" stroke-width="2.2"/></svg>Professionally-designed 1-page or 5-page website (Home, About Us,<br>Services, Contact Us, News)</li>
    <li><svg viewBox="0 0 12 11"><path d="M1 6l3 3 7-8" fill="none" stroke="#fff" stroke-width="2.2"/></svg>Responsive design that displays properly on mobiles and tablets</li>
    <li><svg viewBox="0 0 12 11"><path d="M1 6l3 3 7-8" fill="none" stroke="#fff" stroke-width="2.2"/></svg>On-going changes and updates</li>
    <li><svg viewBox="0 0 12 11"><path d="M1 6l3 3 7-8" fill="none" stroke="#fff" stroke-width="2.2"/></svg>All text written for you</li>
    <li><svg viewBox="0 0 12 11"><path d="M1 6l3 3 7-8" fill="none" stroke="#fff" stroke-width="2.2"/></svg>Photographs (Royalty-free stock images)</li>
    <li><svg viewBox="0 0 12 11"><path d="M1 6l3 3 7-8" fill="none" stroke="#fff" stroke-width="2.2"/></svg>Professional email addresses e.g. info@yourcompany.co.uk,<br>sales@yourcompany.co.uk and yourname@yourcompany.co.uk.<br>We’ll even set up these email addresses on your PC and laptop!</li>
    <li><svg viewBox="0 0 12 11"><path d="M1 6l3 3 7-8" fill="none" stroke="#fff" stroke-width="2.2"/></svg>Links to your social media accounts</li>
    <li><svg viewBox="0 0 12 11"><path d="M1 6l3 3 7-8" fill="none" stroke="#fff" stroke-width="2.2"/></svg>Up to 2 hours’ changes each month to content, pix, and<br>adding new pages</li>
    <li><svg viewBox="0 0 12 11"><path d="M1 6l3 3 7-8" fill="none" stroke="#fff" stroke-width="2.2"/></svg>Professional hosting for your website and email</li>
    <li><svg viewBox="0 0 12 11"><path d="M1 6l3 3 7-8" fill="none" stroke="#fff" stroke-width="2.2"/></svg>No upfront cost! Just weekly, monthly or annual invoice - you choose!</li>
  </ul>
  <p class="fee">For an-all-in fee from only £5 per week for a 1-page website or<br>£10 per week for a 5-page website.</p>
  <div class="trades-photos">
    <div class="photo-electrician" role="img" aria-label="Electrician working on a wall socket"></div>
    <div class="photo-tiler" role="img" aria-label="Tiler levelling floor tiles"></div>
    <div class="photo-plumber" role="img" aria-label="Plumber fixing pipework under a sink"></div>
  </div>
  <div class="offer-band"><span class="promo">PROMOTIONAL</span></div>
  <div class="offer-tab">
    <svg width="193" height="48" viewBox="0 0 193 48"><polygon points="0,0 193,0 193,48 34,48" fill="#e31b2d"/></svg>
    <span>OFFER</span>
  </div>
  <div class="orange-band">order your new 5-page website before ............<br>and we’ll set up a Chatterbox Page for FREE.<br>Normal Cost: £97 plus VAT!</div>
  <div class="contact">
    <p class="line address"><svg viewBox="0 0 10 10"><path d="M5 0a3.4 3.4 0 0 0-3.4 3.4C1.6 6 5 10 5 10s3.4-4 3.4-6.6A3.4 3.4 0 0 0 5 0zm0 4.8a1.4 1.4 0 1 1 0-2.8 1.4 1.4 0 0 1 0 2.8z" fill="#1a1a1a"/></svg>14 Mill Lane, Harwick, HW2 7QT, Lancashire, UK</p>
    <p class="line"><svg viewBox="0 0 10 10"><rect x="0.5" y="2" width="9" height="6" fill="#1a1a1a"/><path d="M0.5 2l4.5 3.5L9.5 2" fill="none" stroke="#fff" stroke-width="0.8"/></svg>info@soloworkswebsites.co.uk<span class="gap"></span><svg viewBox="0 0 10 10"><circle cx="5" cy="5" r="4.3" fill="none" stroke="#1a1a1a" stroke-width="1"/><path d="M0.7 5h8.6M5 0.7v8.6" stroke="#1a1a1a" stroke-width="0.8"/></svg>www.soloworkswebsites.co.uk</p>
    <p class="call">CALL NOW <span class="number">01632 960 418</span></p>
    <p class="terms">For further information or to order.&nbsp;&nbsp; Full terms and conditions at www. TBC.&nbsp; All fees plus VAT.</p>
  </div>
</section>

</body>
</html>
```